Bows Catalog Cover

Cover Page for a catalog for bows. Same logo MOR Morvane Alpina Cordaria.
Catalog overview: https://www.folioworks-demo.net/MOR-Morvane-Alpina-Cordaria/catalogs/MOR-catalog.html
No instruments, no scores, Only bows or bow parts (head, frog ...). Drawings or pictures.

Target Market(s)

Violin makers and reseller

Requirements
Must have
• bows or bow parts
Nice to have
• Drawings and or pictures
Should not have
• full Instruments or scores

```html
<!DOCTYPE html>
<html lang="en">
<head>
<meta charset="utf-8">
<title>Bows Catalog Cover – MOR Morvane Alpina Cordaria</title>
<link rel="stylesheet" href="https://fonts.googleapis.com/css2?family=Anton&family=Josefin+Sans:wght@300;600&family=Montserrat:wght@400&family=Poppins:wght@400&display=swap">
<style>
  :root {
    --board: #d9d9d9;
    --board-heading: #bcbcbc;
    --label: #1e1e1e;
    --cover: #ffffff;
    --magenta: #a21f8c;
    --indigo: #2f2d8f;
    --violet: #5c5ac8;
    --grey-word: #b9b9b9;
    --watermark: #ececec;
    --url-blue: #3a3a9a;
    --url-dark: #1c1c1c;
    --photo-dark: #2a2420;
    --photo-wood: #c9ae78;
  }
  * { margin: 0; padding: 0; box-sizing: border-box; }
  html, body { width: 1200px; height: 908px; overflow: hidden; }
  body {
    position: relative;
    background: var(--board);
    font-family: "Montserrat", sans-serif;
  }
  .board-heading {
    position: absolute;
    left: -8px;
    top: -40px;
    font-family: "Anton", sans-serif;
    font-size: 156px;
    line-height: 1;
    letter-spacing: 1px;
    color: var(--board-heading);
    white-space: nowrap;
  }
  .sample-label {
    position: absolute;
    top: 143px;
    width: 454px;
    text-align: center;
    font-family: "Poppins", sans-serif;
    font-size: 17px;
    letter-spacing: 2.5px;
    color: var(--label);
  }
  .sample-label--one { left: 102px; }
  .sample-label--two { left: 653px; }

  .cover {
    position: absolute;
    top: 188px;
    width: 454px;
    height: 642px;
    background:
      radial-gradient(ellipse 90% 18% at 60% 12%, rgba(0,0,0,0.045), transparent 70%),
      linear-gradient(180deg, #f6f6f6 0%, var(--cover) 18%);
    box-shadow: 0 14px 34px rgba(0,0,0,0.18);
    overflow: hidden;
  }
  .cover--one { left: 102px; }
  .cover--two { left: 653px; }

  .watermark {
    position: absolute;
    display: flex;
    align-items: center;
    gap: 14px;
    font-family: "Josefin Sans", sans-serif;
    font-weight: 600;
    font-size: 64px;
    letter-spacing: 4px;
    line-height: 1;
    color: var(--watermark);
  }
  .watermark-dot {
    width: 110px;
    height: 110px;
    border-radius: 50%;
    background: var(--watermark);
  }
  .cover--one .watermark { left: 214px; top: 430px; }
  .cover--two .watermark { left: 180px; top: 385px; }

  .brand {
    position: absolute;
    top: 32px;
    display: flex;
    align-items: center;
    gap: 10px;
    font-family: "Josefin Sans", sans-serif;
    font-weight: 600;
    font-size: 40px;
    letter-spacing: 4px;
    color: var(--magenta);
    line-height: 1;
  }
  .brand-dot {
    width: 38px;
    height: 38px;
    border-radius: 50%;
    background: var(--magenta);
  }
  .cover--one .brand { left: 132px; }
  .cover--two .brand { left: 148px; }

  .title { position: absolute; overflow: visible; }
  .title text { font-family: "Josefin Sans", sans-serif; }
  .title .word-one { fill: var(--magenta); font-weight: 600; }
  .title .word-two { fill: var(--indigo); font-weight: 600; }
  .title .word-three { fill: var(--grey-word); font-weight: 300; }

  .cover--one .title { left: 99px; top: 112px; width: 258px; height: 210px; }
  .cover--two .title { left: 145px; top: 114px; width: 263px; height: 226px; }

  .artwork { position: absolute; left: 0; top: 0; }

  .site-url {
    position: absolute;
    font-size: 9.5px;
    white-space: nowrap;
  }
  .cover--one .site-url { left: 271px; top: 606px; color: var(--url-blue); }
  .cover--two .site-url { left: 248px; top: 593px; color: var(--url-dark); letter-spacing: 1.1px; }
</style>
</head>
<body>
  <div class="board-heading">BOWS CATALOG COVER</div>

  <div class="sample-label sample-label--one">SAMPLE 1</div>
  <div class="sample-label sample-label--two">SAMPLE 2</div>

  <section class="cover cover--one">
    <div class="watermark" aria-hidden="true"><span class="watermark-dot"></span>MOR</div>

    <svg class="artwork" width="454" height="642" viewBox="0 0 454 642" role="img" aria-label="Photograph of violin bow frogs and sticks in ebony and pernambuco, laid diagonally">
      <defs>
        <linearGradient id="bowPhoto" x1="0" y1="0" x2="1" y2="1">
          <stop offset="0" stop-color="var(--photo-wood)"/>
          <stop offset="0.45" stop-color="#8a7350"/>
          <stop offset="1" stop-color="var(--photo-dark)"/>
        </linearGradient>
      </defs>
      <polygon points="0,287 316,466 316,490 254,594 0,460" fill="url(#bowPhoto)"/>
    </svg>

    <div class="brand"><span class="brand-dot"></span>MOR</div>

    <svg class="title" viewBox="0 0 258 210">
      <text class="word-one" x="0" y="74" font-size="90" textLength="258" lengthAdjust="spacingAndGlyphs">MORVANE</text>
      <text class="word-two" x="0" y="144" font-size="82" textLength="258" lengthAdjust="spacingAndGlyphs">ALPINA</text>
      <text class="word-three" x="0" y="206" font-size="64" textLength="258" lengthAdjust="spacingAndGlyphs">CORDARIA</text>
    </svg>

    <div class="site-url">www.morvane-alpina-cordaria.com</div>
  </section>

  <section class="cover cover--two">
    <div class="watermark" aria-hidden="true"><span class="watermark-dot"></span>MOR</div>

    <svg class="artwork" width="454" height="642" viewBox="0 0 454 642" role="img" aria-label="Flat graphic illustration of a violin bow: stick and frog running down the left edge, bow head along the bottom">
      <defs>
        <linearGradient id="bowArea" x1="0" y1="0" x2="0" y2="1">
          <stop offset="0" stop-color="var(--magenta)"/>
          <stop offset="1" stop-color="var(--violet)"/>
        </linearGradient>
      </defs>
      <rect x="35" y="0" width="78" height="614" fill="url(#bowArea)"/>
      <rect x="113" y="556" width="341" height="58" fill="var(--violet)"/>
    </svg>

    <div class="brand"><span class="brand-dot"></span>MOR</div>

    <svg class="title" viewBox="0 0 263 226">
      <text class="word-one" x="0" y="77" font-size="96" textLength="263" lengthAdjust="spacingAndGlyphs">MORVANE</text>
      <text class="word-two" x="0" y="154" font-size="90" textLength="263" lengthAdjust="spacingAndGlyphs">ALPINA</text>
      <text class="word-three" x="0" y="220" font-size="72" textLength="218" lengthAdjust="spacingAndGlyphs">CORDARIA</text>
    </svg>
  </section>
  <div class="site-url" style="position:absolute;left:901px;top:781px;font-size:9.5px;letter-spacing:1.1px;color:#ffffff;white-space:nowrap;">www.morvane-alpina-cordaria.com</div>
</body>
</html>
```